Manuka honey wholesales and exports

We need business cards for our honey distribution company based in New Zealand. We supply shops locally and export Manuka honey around the world.
We deal with a very high quality and 100% natural product that can be used for medical, general health as well as food. We are looking business cards that show our honey products are of a high quality with a modern look.

Target Market(s)

Health and medical retailers and importers

Industry/Entity Type

Wholesale

Contact Information for Business Card

Tevin Apiary NZ Limited

www.tevinapiarynz.example

Derek Fawley

M +64 219036482

E tevinapiarynz@mailbox.example

PO Box 58-214
Takapuna
North Shore
Auckland
New Zealand

Font styles to use
Serif

Requirements
Must have
• (Tevin Apiary NZ Limited) with some artwork on one side and all details on the other side.
Nice to have
• I have seen a very simple card with large yellow and black stripes on one side with a company name.. looked clean and simple so something similar or just let the creative beast inside you take over and we will see what you can come up with.

```html
<!DOCTYPE html>
<html lang="en">
<head>
<meta charset="utf-8">
<title>Tevin Apiary NZ Limited – Business Card</title>
<link rel="stylesheet" href="https://fonts.googleapis.com/css2?family=DM+Serif+Display&display=swap">
<style>
  :root {
    --backdrop: #c2b4b4;
    --ink: #060709;
    --ink-soft: #4a4a4d;
    --honey: #fcd80a;
    --honey-deep: #f7a31b;
    --stripe-yellow: #fbc21b;
    --text-dark: #1c1a17;
    --text-light: #ffffff;
  }
  * { margin: 0; padding: 0; box-sizing: border-box; }
  html, body {
    width: 1200px; height: 1000px; overflow: hidden;
    background: var(--backdrop);
  }
  .canvas { position: relative; width: 1200px; height: 1000px; }
  .card {
    position: absolute; left: 284px; width: 617px; height: 400px;
    overflow: hidden;
    box-shadow: 0 1px 3px rgba(0,0,0,0.25);
    font-family: "DM Serif Display", Georgia, serif;
  }
  .card-front {
    top: 66px;
    background: radial-gradient(circle at 3% 97%, var(--ink-soft) 0%, #1c1c1e 28%, var(--ink) 55%);
  }
  .card-back {
    top: 519px;
    background: linear-gradient(215deg, var(--honey-deep) 0%, #fbc511 25%, var(--honey) 50%, var(--honey) 100%);
  }
  .stripes { position: absolute; inset: 0; width: 617px; height: 400px; }
  .company-name {
    position: absolute; right: 153px; top: 38px;
    text-align: right; color: var(--text-light); line-height: 1;
  }
  .company-name .line-1 { display: block; font-size: 94px; }
  .company-name .line-2 { display: block; font-size: 88px; margin-top: -4px; }
  .company-name .line-3 { display: block; font-size: 50px; margin-top: 14px; }
  .details { position: absolute; left: 259px; top: 36px; color: var(--text-dark); }
  .person-name { font-size: 40px; line-height: 1; letter-spacing: 0.5px; }
  .contact { margin-top: 36px; font-size: 17px; line-height: 23px; }
  .address { margin-top: 19px; font-size: 19px; line-height: 26.5px; }
  .website {
    position: absolute; left: 38px; top: 328px;
    font-size: 28px; color: var(--text-light);
    text-shadow: 1px 2px 3px rgba(90,60,0,0.55);
  }
</style>
</head>
<body>
<div class="canvas">

  <section class="card card-front">
    <svg class="stripes" viewBox="0 0 617 400" aria-hidden="true">
      <g fill="var(--stripe-yellow)">
        <polygon points="2,0 18,0 -237,400 -253,400"/>
        <polygon points="34,0 70,0 -185,400 -221,400"/>
        <polygon points="700,0 738,0 483,400 445,400"/>
        <polygon points="768,0 808,0 553,400 513,400"/>
        <polygon points="838,0 880,0 625,400 583,400"/>
      </g>
    </svg>
    <h1 class="company-name">
      <span class="line-1">Tevin</span>
      <span class="line-2">Apiary</span>
      <span class="line-3">NZ Limited</span>
    </h1>
  </section>

  <section class="card card-back">
    <svg class="stripes" viewBox="0 0 617 400" aria-hidden="true">
      <defs>
        <linearGradient id="stripe-sheen" x1="0" y1="0" x2="1" y2="0.6">
          <stop offset="0" stop-color="#0a0a0a"/>
          <stop offset="0.3" stop-color="#3b3b3d"/>
          <stop offset="0.6" stop-color="#0a0a0a"/>
          <stop offset="1" stop-color="#111"/>
        </linearGradient>
      </defs>
      <g fill="url(#stripe-sheen)">
        <polygon points="18,0 58,0 -197,400 -237,400"/>
        <polygon points="92,0 140,0 -115,400 -163,400"/>
        <polygon points="166,0 213,0 -42,400 -89,400"/>
      </g>
      <g fill="var(--ink)">
        <polygon points="790,0 814,0 559,400 535,400"/>
        <polygon points="828,0 850,0 595,400 573,400"/>
        <polygon points="864,0 884,0 629,400 609,400"/>
      </g>
    </svg>
    <div class="details">
      <h2 class="person-name">Derek Fawley</h2>
      <p class="contact">M: +64 219036482<br>E: tevinapiarynz@mailbox.example</p>
      <address class="address" style="font-style:normal">
        PO Box 58-214<br>Takapuna<br>North Shore<br>Auckland<br>New Zealand
      </address>
    </div>
    <p class="website">www.tevinapiarynz.example</p>
  </section>

</div>
</body>
</html>
```